Notary Signing Agent Need Business card Design

Need a Business card design for my new company. RT Belvoni-Strand LLC
Mobile Notary Signing Agent. I go to the customer for closing of Mortgage's Documents . possible signs of honesty, integrity and confidentiality.

Work with Title company to Notary Mortgage closing.

My Target Market is Title companies. Banks and Financial Institution.

Color Blue to Black Professional ) if needed some Green Little Red

And possible a company logo.

Mobile ( travel to clients ) Integrity, Honest Trustworthy. A show of Professional services.

Would like company name and my name on card

Use both sides and front with business name and my name. phone numbers.

Target Market(s)

Title company, Banks mortgage company

Industry/Entity Type

Travel

Contact Information for Business Card

Notary, Certified signing agent, Mobile

Colors
0455a3

Requirements
Must have
• Name of company , owners name phone number,
Nice to have
• blue and black color like a professional look but not limit to these only.
• a stand out from other cards .

```html
<!DOCTYPE html>
<html lang="en">
<head>
<meta charset="utf-8">
<title>RT Belvoni-Strand LLC — Business Card</title>
<link rel="stylesheet" href="https://fonts.googleapis.com/css2?family=Exo+2:wght@300;400;600&display=swap">
<style>
  :root {
    --stage: #1d1e20;
    --card: #0d0e10;
    --green: #1f7048;
    --blue: #0c5f93;
    --white: #eef1f3;
    --muted: #c9cfd4;
  }
  * { margin: 0; padding: 0; box-sizing: border-box; }
  html, body { width: 1200px; height: 659px; overflow: hidden; }
  body {
    background: var(--stage);
    font-family: "Exo 2", Arial, sans-serif;
    position: relative;
  }
  .card {
    position: absolute;
    top: 178px;
    width: 530px;
    height: 303px;
    background: var(--card);
    box-shadow: 0 6px 18px rgba(0,0,0,.45);
  }
  .card--front { left: 50px; }
  .card--back { left: 620px; }
  .card__frame { position: absolute; inset: 0; }
  .company-name {
    color: var(--green);
    font-weight: 600;
    font-size: 30px;
    letter-spacing: .5px;
    white-space: nowrap;
    display: flex;
    align-items: center;
    gap: 10px;
  }
  .company-name__mark {
    width: 16px; height: 16px;
    background: var(--green);
  }
  .card--front .company-name {
    position: absolute; top: 56px; left: 90px;
  }
  .contact {
    position: absolute; top: 112px; left: 205px;
    color: var(--white);
    text-align: left;
  }
  .contact__name {
    font-size: 22px; font-weight: 400;
    border-bottom: 1px solid var(--muted);
    padding-bottom: 3px; margin-bottom: 4px;
  }
  .contact__title {
    font-size: 12px; font-weight: 300; color: var(--muted);
    margin-bottom: 8px;
  }
  .contact__phone {
    font-size: 20px; font-weight: 300; letter-spacing: 1px; line-height: 1.2;
  }
  .card--back .company-name {
    position: absolute; top: 128px; left: 0; right: 0;
    justify-content: center; font-size: 32px;
  }
</style>
</head>
<body>
  <section class="card card--front" aria-label="Business card front">
    <svg class="card__frame" width="530" height="303" viewBox="0 0 530 303" aria-hidden="true">
      <polyline points="30,24 504,24 504,268" fill="none" stroke="var(--green)" stroke-width="8"/>
      <polyline points="24,34 24,279 494,279" fill="none" stroke="var(--blue)" stroke-width="8"/>
    </svg>
    <div class="company-name"><span class="company-name__mark"></span>RT Belvoni-Strand LLC</div>
    <div class="contact">
      <p class="contact__name">Daniel R. Kessor</p>
      <p class="contact__title">Notary Certified Signing Agent</p>
      <p class="contact__phone">850-555-0142</p>
      <p class="contact__phone">860-555-0187</p>
    </div>
  </section>

  <section class="card card--back" aria-label="Business card back">
    <svg class="card__frame" width="530" height="303" viewBox="0 0 530 303" aria-hidden="true">
      <polyline points="30,24 504,24 504,268" fill="none" stroke="var(--green)" stroke-width="8"/>
      <polyline points="24,34 24,279 494,279" fill="none" stroke="var(--blue)" stroke-width="8"/>
    </svg>
    <div class="company-name"><span class="company-name__mark"></span>RT Belvoni-Strand LLC</div>
  </section>
</body>
</html>
```